Rebrand & reskin runpulse.net (Uncoded)

Runpulse.net is a commerce website and app for sports and fitness classes and events. In order to improve its appeal, we invite designers to provide their 'skins' for the landing page, club page and event page. Designers can propose using alternate controls and layouts for these pages, and comment on ways to improve the site's usability. It must remain easy to use on a portrait mobile phone screen, responsive design where necessary to also provide a good experience on desktop.

Please navigate to runpulse.net and explore the site, and we look forwards to your suggestions!

Target Market(s)

Primary: Tech-savvy mobile users. Secondary: Desktop users

Industry/Entity Type

Health And Wellness

Number of Pages Required

3 page

Font styles to use
Sans Serif

Colors
ffffff
f37122

Requirements
Must have
• This brief is all about changing the look and feel of the site; the winning design will have an immediate 'wow' factor, yet not sacrifice the ease of finding and paying for classes. It must retain the logo, white and orange must be the primary colours used.
Should not have
• The colour palette must remain roughly as is; for example, a very dark site will not appeal.

```html
<!DOCTYPE html>
<html lang="en">
<head>
<meta charset="utf-8">
<title>Runpulse.net – Events</title>
<link href="https://fonts.googleapis.com/css2?family=Open+Sans:wght@400;600&family=Roboto:wght@400;500&display=swap" rel="stylesheet">
<style>
:root{
  --orange:#f37122;
  --orange-deep:#ee5a1a;
  --white:#ffffff;
  --ink:#3a3a3f;
  --muted:#8a8a8a;
  --side:#4a4a53;
  --side-line:#5d5d66;
  --bar-top:#5a5a63;
  --bar-bottom:#2f2f35;
  --footer:#2c2c2e;
  --stone:#e6e6e6;
  --rule:#d8d8d8;
}
*{margin:0;padding:0;box-sizing:border-box}
html,body{width:1200px;height:1049px;overflow:hidden}
body{position:relative;font-family:"Open Sans",sans-serif;background:radial-gradient(ellipse at 60% 40%,#f0f0f0,#dedede);color:var(--ink)}
.abs{position:absolute}
.header{left:0;top:0;width:1200px;height:102px;background:var(--white);border-bottom:1px solid var(--rule)}
.brand{left:117px;top:33px;display:flex;align-items:center;gap:10px;font-family:"Roboto",sans-serif;font-weight:500;font-size:28px;color:var(--orange);letter-spacing:1px}
.brand-dot{width:40px;height:40px;border-radius:50%;background:var(--orange)}
.nav{left:0;top:0;height:102px}
.nav a{position:absolute;top:0;height:102px;display:flex;align-items:center;justify-content:center;font-family:"Roboto",sans-serif;font-size:17px;color:#4a4a4a;text-decoration:none;border-left:1px solid var(--rule)}
.nav a.first{border-left:none}
.nav a.active{background:linear-gradient(#4a4a50,#2a2a2e);color:var(--white);border-left:none}
.sidebar{left:105px;top:102px;width:223px;height:879px;background:var(--side)}
.side-item{height:57px;display:flex;align-items:center;border-bottom:1px solid var(--side-line);color:var(--white);font-family:"Roboto",sans-serif;font-size:17px;padding-left:68px;position:relative}
.side-item:last-child{border-bottom:none}
.side-item svg{position:absolute;left:30px;top:50%;transform:translateY(-50%)}
.page-title{left:366px;top:140px;font-family:"Roboto",sans-serif;font-size:30px;color:#444;letter-spacing:1px}
.panel{left:364px;top:206px;width:708px;height:775px;background:var(--white);border:1px solid var(--rule)}
.bar{position:absolute;left:0;width:708px;height:43px;display:flex;align-items:center;justify-content:space-between;padding:0 22px 0 20px;font-family:"Roboto",sans-serif;font-size:16.5px;font-weight:500;color:var(--white)}
.bar.open{top:0;height:42px;background:linear-gradient(var(--orange),var(--orange-deep))}
.bar.closed{background:linear-gradient(var(--bar-top),var(--bar-bottom));border-bottom:1px solid #6a6a72}
.event-name{left:405px;top:277px;font-size:16px;color:var(--orange)}
.event-desc{left:405px;top:304px;width:340px;font-size:12.5px;line-height:21px;color:var(--muted)}
.map{left:758px;top:277px;width:290px;height:182px;background:linear-gradient(135deg,#ecebe4,#f6f5ef 50%,#e8e6dc);border:1px solid #d4d4d4}
.attending{left:405px;top:388px;font-size:14.5px;color:#222}
.person{left:398px;display:flex;align-items:center;gap:8px;font-size:15px;color:var(--muted)}
.avatar{width:53px;height:53px;border-radius:50%;background:linear-gradient(#b9a48e,#6b5c50)}
.tabs{left:394px;top:569px;width:655px;height:215px}
.tab{position:absolute;top:0;height:36px;display:flex;align-items:center;justify-content:center;font-family:"Roboto",sans-serif;font-size:14.5px}
.tab.comment{left:0;width:114px;background:var(--white);color:var(--orange);border:1px solid #bbb;border-bottom:none;z-index:2;height:37px}
.tab.review{left:114px;width:105px;background:var(--side);color:var(--white)}
.tab-body{position:absolute;top:36px;left:0;width:655px;height:179px;border:1px solid #bbb;box-shadow:0 1px 2px rgba(0,0,0,.15)}
.comment-box{position:absolute;left:25px;top:14px;width:602px;height:88px;border:1px solid #ccc;background:linear-gradient(#fff,#efefef);padding:11px 15px;font-size:13px;color:#888}
.post{position:absolute;left:25px;top:108px;width:98px;height:35px;background:var(--orange);color:var(--white);font-family:"Roboto",sans-serif;font-size:16px;display:flex;align-items:center;justify-content:center}
.footer{left:0;top:981px;width:1200px;height:68px;background:var(--footer);color:#bdbdbd;font-size:13.5px;display:flex;align-items:center;justify-content:center}
</style>
</head>
<body>
<header class="abs header">
  <div class="abs brand"><span class="brand-dot"></span>RUNPULSE</div>
  <nav class="abs nav">
    <a class="first" style="left:430px;width:145px">CALENDAR</a>
    <a style="left:575px;width:110px">FEED</a>
    <a style="left:685px;width:142px">NEAR BY</a>
    <a style="left:827px;width:139px">CLASSES</a>
    <a class="active" style="left:966px;width:115px">EVENT</a>
  </nav>
</header>

<aside class="abs sidebar">
  <div class="side-item" style="height:70px">
    <svg width="26" height="22" viewBox="0 0 26 22"><path d="M14 2h8a2 2 0 0 1 2 2v14a2 2 0 0 1-2 2h-8" fill="none" stroke="#fff" stroke-width="2.5"/><path d="M2 8h8V3l8 8-8 8v-5H2z" fill="#fff"/></svg>LOGIN</div>
  <div class="side-item">
    <svg width="24" height="28" viewBox="0 0 24 28"><rect x="2" y="2" width="20" height="24" rx="2" fill="none" stroke="#fff" stroke-width="2.2"/><rect x="9" y="0" width="6" height="6" fill="#fff"/><path d="M15 14l1.2 2.6 2.8.3-2 1.9.5 2.8-2.5-1.4-2.5 1.4.5-2.8-2-1.9 2.8-.3z" fill="#fff"/></svg>MY DIARY</div>
  <div class="side-item">
    <svg width="36" height="36" viewBox="0 0 36 36" style="left:22px"><path d="M18 1l17 17-17 17L1 18z" fill="#fff"/><path d="M9 18h18M11 13v10M25 13v10" stroke="#4a4a53" stroke-width="4"/></svg>MY CLUBS</div>
  <div class="side-item">
    <svg width="26" height="28" viewBox="0 0 26 28" style="left:36px"><circle cx="13" cy="8" r="7" fill="#fff"/><path d="M0 28v-5c0-5 4-8 8-8h10c4 0 8 3 8 8v5z" fill="#fff"/></svg>MY PROFILE</div>
</aside>

<h1 class="abs page-title" style="font-weight:400">EVENTS</h1>

<section class="abs panel">
  <div class="bar open">EVENT TITTLE HERE
    <svg width="22" height="12" viewBox="0 0 22 12"><path d="M1 11L11 2l10 9" fill="none" stroke="#fff" stroke-width="2"/></svg>
  </div>
  <div class="bar closed" style="top:601px">EVENT TITTLE HERE
    <svg width="22" height="12" viewBox="0 0 22 12"><path d="M1 1l10 9 10-9" fill="none" stroke="#fff" stroke-width="2"/></svg></div>
  <div class="bar closed" style="top:644px">EVENT TITTLE HERE
    <svg width="22" height="12" viewBox="0 0 22 12"><path d="M1 1l10 9 10-9" fill="none" stroke="#fff" stroke-width="2"/></svg></div>
  <div class="bar closed" style="top:687px">EVENT TITTLE HERE
    <svg width="22" height="12" viewBox="0 0 22 12"><path d="M1 1l10 9 10-9" fill="none" stroke="#fff" stroke-width="2"/></svg></div>
</section>

<h2 class="abs event-name" style="font-weight:400">Event Name Here</h2>
<p class="abs event-desc">Praesent sit amet est In dictum dolor eu dictum porttitor enim felis viverra mi eget luctus massa purus quis odio Etiam nulla massa pharetra facilisis volutpat</p>
<div class="abs map" role="img" aria-label="Street map showing the event location"></div>

<h3 class="abs attending" style="font-weight:400">Who’s attending the Event</h3>
<div class="abs person" style="top:419px"><div class="avatar" role="img" aria-label="Profile photo of Daniel Hartley"></div>Daniel Hartley</div>
<div class="abs person" style="top:481px"><div class="avatar" role="img" aria-label="Profile photo of Clara Benning"></div>Clara Benning</div>

<div class="abs tabs">
  <div class="tab comment">COMMENT</div>
  <div class="tab review">REVIEW</div>
  <div class="tab-body">
    <div class="comment-box">Type your comment here</div>
    <div class="post">POST</div>
  </div>
</div>

<footer class="abs footer">© 2016 Company Name&nbsp; All right reserved&nbsp; Term of Use</footer>
</body>
</html>
```